professional business card design

Business card design. Photos have been uploaded and i am open to the designer choosing which photos to use. Would like the card to be mostyly in a grey scale design with black, whites, silver & grey colours. I have added copy of our flyer as would like on the back side of card our services to be listed. Do not use any bright colurs such as blue red green or yellow. i need to be able to edit the phone number and naem in the final card design submitted.

Target Market(s)

Clients

Industry/Entity Type

earhmovibng and transport

Contact Information for Business Card

Director Name, address, email, phone number and services

Colors

Designer to choose only greyscale colors for use in the design.

Requirements
Should not have
• no yellow, red, blue or green

```html
<!DOCTYPE html>
<html lang="en">
<head>
<meta charset="utf-8">
<title>Ridgeline Haul Services – Business Card</title>
<link href="https://fonts.googleapis.com/css2?family=Barlow:wght@400;600;700&family=Barlow+Condensed:wght@400;500&family=Barlow+Semi+Condensed:wght@400;700&display=swap" rel="stylesheet">
<style>
  :root {
    --page: #ffffff;
    --ink: #111111;
    --ink-soft: #262626;
    --night: #060608;
    --logo-dark: #2a2a2c;
    --logo-light: #c4c4c6;
  }
  * { box-sizing: border-box; margin: 0; padding: 0; }
  html, body {
    width: 1200px; height: 846px; overflow: hidden;
    background: var(--page);
    font-family: "Barlow Semi Condensed", "Barlow", Arial, sans-serif;
    color: var(--ink);
  }
  .card {
    position: absolute; left: 347px; width: 509px; height: 291px;
    border-radius: 26px; overflow: hidden;
    box-shadow: 6px 10px 14px rgba(0,0,0,0.14);
  }
  .card--front { top: 99px; }
  .card--back { top: 458px; }
  .card__bg { position: absolute; inset: 0; width: 100%; height: 100%; }

  .brand {
    position: absolute; font-family: "Barlow", Arial, sans-serif;
    font-weight: 700; letter-spacing: 2px; line-height: 1; font-size: 50px;
  }
  .card--front .brand { left: 28px; top: 20px; color: var(--logo-dark); }
  .card--back .brand { left: 330px; top: 210px; color: var(--logo-light); }

  .person { position: absolute; left: 45px; top: 80px; }
  .person__name { font-size: 15px; font-weight: 700; line-height: 18px; }
  .person__role { font-size: 12.5px; font-weight: 400; line-height: 16px; color: var(--ink-soft); }

  .contact { position: absolute; left: 25px; top: 122px; list-style: none; }
  .contact__item {
    display: flex; align-items: flex-start; gap: 5px;
    font-size: 13px; line-height: 14px; color: var(--ink-soft);
    margin-bottom: 4.5px; white-space: nowrap;
  }
  .contact__icon { width: 15px; height: 14px; flex: none; fill: var(--ink); }

  .photo { position: absolute; }
  .photo--front {
    left: 222px; top: 27px; width: 253px; height: 228px; border-radius: 10px;
    background: radial-gradient(ellipse at 60% 55%, #e8e8e8 0%, #9a9a9a 45%, #3a3a3a 80%, rgba(20,20,20,0) 100%);
  }
  .photo--back {
    left: 29px; top: 121px; width: 266px; height: 159px; border-radius: 8px;
    background: linear-gradient(100deg, #9c9c9c 0%, #3c3c3c 35%, #555 60%, #2a2a2a 100%);
  }

  .services {
    position: absolute; top: 30px; list-style: none; width: 122px;
    font-family: "Barlow Condensed", "Arial Narrow", sans-serif;
    font-weight: 500; font-size: 11.5px; letter-spacing: -0.2px;
    line-height: 16px; color: var(--ink); white-space: nowrap;
  }
  .services li { padding-left: 5px; text-indent: -5px; }
  .services li::before { content: "▪ "; font-size: 7px; vertical-align: 2px; }
  .services--one { left: 29px; }
  .services--two { left: 157px; }
  .services--three { left: 287px; }
</style>
</head>
<body>

<section class="card card--front" aria-label="Business card front">
  <svg class="card__bg" viewBox="0 0 509 291" preserveAspectRatio="none" aria-hidden="true">
    <defs>
      <linearGradient id="silverFront" x1="0" y1="0" x2="1" y2="0">
        <stop offset="0" stop-color="#b9b9bb"/>
        <stop offset="0.35" stop-color="#f3f3f4"/>
        <stop offset="0.6" stop-color="#d0d0d2"/>
        <stop offset="1" stop-color="#9b9b9e"/>
      </linearGradient>
      <linearGradient id="chromeFront" x1="0" y1="0" x2="1" y2="0">
        <stop offset="0" stop-color="#8a8a8c"/>
        <stop offset="0.3" stop-color="#fbfbfb"/>
        <stop offset="0.65" stop-color="#a4a4a6"/>
        <stop offset="1" stop-color="#5c5c5e"/>
      </linearGradient>
    </defs>
    <rect width="509" height="291" fill="url(#silverFront)"/>
    <path d="M0,212 C120,262 220,228 300,152 C370,104 440,94 509,97 L509,291 L0,291 Z" fill="url(#chromeFront)"/>
    <path d="M0,230 C120,272 232,244 312,174 C382,124 440,112 509,116 L509,291 L0,291 Z" fill="var(--night)"/>
  </svg>

  <div class="brand">RHS</div>

  <div class="photo photo--front" role="img" aria-label="Photo of a road train tanker truck, front three-quarter view"></div>

  <div class="person">
    <p class="person__name">Daniel Varga</p>
    <p class="person__role">director</p>
  </div>

  <ul class="contact">
    <li class="contact__item">
      <svg class="contact__icon" viewBox="0 0 16 16" aria-hidden="true"><path d="M6 1 L8 1 L8 5 L6 6 C6 9 6.5 11 7.5 12 L9 11.5 L10 15 L8 15.5 C4.5 15 3 11 3.2 7 C3.4 3.5 4.5 1.5 6 1 Z"/></svg>
      <span>Tel. 000 444 000</span>
    </li>
    <li class="contact__item">
      <svg class="contact__icon" viewBox="0 0 16 16" aria-hidden="true"><path d="M1 3 H15 V13 H1 Z M2 4.2 V12 H14 V4.2 L8 9 Z M2.6 4 L8 8.2 L13.4 4 Z" fill-rule="evenodd"/></svg>
      <span>email@ridgelinehaul.com.au</span>
    </li>
    <li class="contact__item">
      <svg class="contact__icon" viewBox="0 0 16 16" aria-hidden="true"><circle cx="8" cy="8" r="7"/><path d="M1 8 H15 M8 1 V15 M3 4 H13 M3 12 H13" stroke="#d8d8d8" stroke-width="0.9" fill="none"/><ellipse cx="8" cy="8" rx="3" ry="7" stroke="#d8d8d8" stroke-width="0.9" fill="none"/></svg>
      <span>www.websiteaddress.com</span>
    </li>
    <li class="contact__item">
      <svg class="contact__icon" viewBox="0 0 16 18" aria-hidden="true"><path d="M8 0.5 C4 0.5 1.5 3.2 1.5 6.5 C1.5 10.5 8 17.5 8 17.5 C8 17.5 14.5 10.5 14.5 6.5 C14.5 3.2 12 0.5 8 0.5 Z M8 4 A2.6 2.6 0 1 1 7.99 4 Z" fill-rule="evenodd"/></svg>
      <span>Lot 114, Ironbark Creek Road,<br>Saltbush Flat, Australia</span>
    </li>
  </ul>
</section>

<section class="card card--back" aria-label="Business card back">
  <svg class="card__bg" viewBox="0 0 509 291" preserveAspectRatio="none" aria-hidden="true">
    <defs>
      <linearGradient id="silverBack" x1="0" y1="0" x2="1" y2="0">
        <stop offset="0" stop-color="#bdbdbf"/>
        <stop offset="0.4" stop-color="#f2f2f3"/>
        <stop offset="0.7" stop-color="#cfcfd1"/>
        <stop offset="1" stop-color="#a3a3a6"/>
      </linearGradient>
      <linearGradient id="chromeBack" x1="0" y1="0" x2="1" y2="0">
        <stop offset="0" stop-color="#8c8c8e"/>
        <stop offset="0.45" stop-color="#f7f7f7"/>
        <stop offset="0.75" stop-color="#9e9ea0"/>
        <stop offset="1" stop-color="#5a5a5c"/>
      </linearGradient>
    </defs>
    <rect width="509" height="291" fill="url(#silverBack)"/>
    <path d="M0,214 C100,236 220,222 290,180 C360,135 430,112 509,110 L509,291 L0,291 Z" fill="url(#chromeBack)"/>
    <path d="M0,242 C110,262 226,248 298,205 C366,165 430,152 509,150 L509,291 L0,291 Z" fill="var(--night)"/>
  </svg>

  <ul class="services services--one">
    <li>Over size loads /<br>Hot Shot Loads</li>
    <li>Heavy Vehicle Recovery<br>Services</li>
    <li>Portable Water Deliveries</li>
  </ul>
  <ul class="services services--two">
    <li>Road Building / Maintenance</li>
    <li>Sand &amp; Metal Supply<br>&amp; Cartage</li>
    <li>Earthworks</li>
    <li>Drop Deck Trailers</li>
  </ul>
  <ul class="services services--three">
    <li>Road Train Tippers</li>
    <li>Road Train Tankers</li>
    <li>Road Train Flat Tops</li>
    <li>Mine Site Accredited<br>Equipment &amp; Operators</li>
  </ul>

  <div class="photo photo--back" role="img" aria-label="Photo of a prime mover hauling a side tipper trailer"></div>

  <div class="brand">RHS</div>
</section>

</body>
</html>
```